Real Estate Website

We need a web design for a new site that is focused on real estate listings and information for the Singapore, Malaysian and Australian market.

The web site will have listings of available real estate for sale, past transaction data on real estate, information about neighborhoods where the real estate is located.
Website URL will likely be www.dwellora.net. We are also open to suggestions on site names (assuming URL is available).

We like the simplicity of a similar US site called Vexomi.com - and want to focus on providing a similar "clean" user interface where users can find the information they need. The final design should be user friendly, be visually compelling with a focus on ease of navigation.

Requirements to have at least 5 web pages designed that will display the data as in the attached document for any given territory. We will need to receive
- HTML/CSS/JavaScript, and all images
- any design icons for common objects (e.g. house/home, map, user, agent, trend chart, contact, bathroom, bedroom, garage, furniture, price, ...etc).
Updates

Hi

I just added more details to the brief and committed to pay for the project.
Please review the additional information and submit your final designs by June 14th (or sooner) as we have a deadline to meet. 

Let me know if you have any questions, I will try to be prompt in my responses. 
Thanks.

Target Market(s)

Consumers who are researching real estate to purchase or sell

Industry/Entity Type

Real Estate

Requirements
Must have
• Data in attached document needs to be displayed.

```html
<!DOCTYPE html>
<html lang="en">
<head>
<meta charset="utf-8">
<title>Dwellora</title>
<link rel="stylesheet" href="https://fonts.googleapis.com/css2?family=Fira+Sans:wght@400;600&family=Gelasio:wght@400;600&family=Noto+Sans:wght@400;700&display=swap">
<style>
:root{
  --page:#efe7d1;
  --panel:#e9dfc6;
  --panel-light:#f4eedd;
  --line:#d8ccae;
  --brown-dark:#5a3e2d;
  --accent:#c4502a;
  --price:#3f7d1b;
  --link:#a4161a;
  --text:#2e2a25;
  --muted:#6a5f50;
  --olive:#8a6a1a;
}
*{box-sizing:border-box;margin:0;padding:0}
html,body{width:900px;height:1200px;overflow:hidden}
body{background:var(--page);font-family:"Noto Sans",sans-serif;color:var(--text);position:relative;font-size:9px}
.abs{position:absolute}
.site-name{left:58px;top:20px;font-family:"Gelasio",serif;font-weight:400;font-size:23px;color:var(--brown-dark)}
.tagline{left:58px;top:45px;font-family:"Noto Sans",sans-serif;font-weight:400;font-size:9.5px;color:var(--muted)}
.toplinks{right:60px;top:6px;font-size:8.5px;color:#333}
.toplinks a{color:var(--link);text-decoration:none}
.toplinks span{color:var(--accent);margin:0 4px}
.submit-btn{left:677px;top:30px;width:166px;height:27px;background:linear-gradient(#7b9a44,#56732a);border-radius:3px;color:#fff;font-family:"Gelasio",serif;font-size:13px;display:flex;align-items:center;justify-content:center;gap:8px}
.nav{left:57px;top:73px;width:786px;height:26px;background:linear-gradient(#6b4b36,#4d3526);border-radius:3px 3px 0 0;display:flex}
.nav a{color:#fff;font-weight:700;font-size:10px;text-decoration:none;display:flex;align-items:center;padding:0 14px;border-right:1px solid #876a55;height:100%}
.featured{left:57px;top:99px;width:786px;height:235px;background:var(--panel);border:1px solid var(--line)}
.hero{left:73px;top:110px;width:425px;height:209px;background:#fff;padding:3px;box-shadow:0 1px 3px rgba(0,0,0,.3)}
.hero-img{width:100%;height:100%;background:linear-gradient(#b7c9dc 0%,#a59080 45%,#5f8a3a 62%,#4c7a2c 100%)}
.hero-cap{left:76px;top:290px;width:419px;height:26px;background:rgba(30,40,20,.55);display:flex;justify-content:space-between;align-items:center;padding:0 14px;font-family:"Gelasio",serif;font-size:13px;color:#fff}
.hero-cap b{color:#f1d36a;font-weight:400}
.ribbon{left:48px;top:119px;width:172px;height:26px;background:linear-gradient(#d8622e,#b2461f);color:#fff;font-family:"Gelasio",serif;font-size:13px;line-height:26px;padding-left:13px;clip-path:polygon(0 0,92% 0,100% 50%,92% 100%,0 100%)}
.thumb{left:508px;width:81px;height:48px;background:#fff;padding:2px;box-shadow:0 1px 2px rgba(0,0,0,.3)}
.thumb div{width:100%;height:100%;background:linear-gradient(135deg,#8a4a26,#d49a64 50%,#5a2f1a)}
.agents{left:607px;top:100px;width:235px;height:233px;background:linear-gradient(90deg,#d9cbb0,#e6dbc2);border-left:1px solid #cbbd9f}
.section-title{font-family:"Gelasio",serif;font-size:13px;color:#3a2f25}
.agent{left:622px;width:213px;height:48px;border-top:1px solid #cdbf9f}
.agent h4{position:absolute;left:12px;top:5px;font-size:9.5px;font-weight:700;color:#3a2f25}
.agent p{position:absolute;left:12px;top:22px;font-size:8px;color:#3a2f25}
.agent .photo{position:absolute;right:6px;top:2px;width:50px;height:40px;background:#fff;padding:2px}
.agent .photo div{width:100%;height:100%;background:linear-gradient(#dfe3e6,#8c96a0)}
.search{left:57px;top:340px;width:786px;height:118px;background:linear-gradient(#9a8572,#85705d);border-radius:4px;color:#fff;font-family:"Gelasio",serif;font-size:11px}
.search .lbl{position:absolute}
.field{position:absolute;height:18px;background:#fff;border-radius:4px}
.select::after{content:"";position:absolute;right:5px;top:4px;width:10px;height:10px;border:1px solid #999;background:#eee}
.radio{display:inline-block;width:10px;height:10px;border-radius:50%;background:#fff;vertical-align:-1px;margin:0 4px 0 10px}
.s-btn{position:absolute;height:22px;background:linear-gradient(#6b5647,#4a3a2f);border-radius:3px;display:flex;align-items:center;gap:6px;padding:0 9px;font-size:11px}
.divider-v{position:absolute;left:596px;top:8px;width:1px;height:100px;background:#a8937e}
.services{left:57px;top:463px;width:786px;height:109px;background:linear-gradient(var(--panel-light),#e2d7bd);border:1px solid var(--line)}
.svc{position:absolute;top:0;height:107px}
.svc h3{position:absolute;left:54px;top:14px;font-family:"Gelasio",serif;font-size:14px;color:var(--link);font-weight:400}
.svc p{position:absolute;left:16px;top:33px;width:230px;font-family:"Gelasio",serif;font-size:10px;line-height:12px;color:#222}
.more{position:absolute;left:18px;top:77px;width:82px;height:14px;background:linear-gradient(#8b7560,#5e4a3a);border-radius:7px;color:#fff;font-size:8px;font-weight:700;display:flex;align-items:center;justify-content:center;gap:4px}
.content{left:57px;top:578px;width:786px;height:378px;background:var(--panel-light);border:1px solid var(--line)}
.listing{left:72px;width:520px;height:100px}
.listing .pic{position:absolute;left:0;top:0;width:149px;height:85px;background:var(--panel);border:1px solid #d6cba9;padding:6px}
.listing .pic div{width:100%;height:100%}
.listing .bar{position:absolute;left:165px;top:0;width:353px;height:23px;background:#e8dfc8;display:flex;align-items:center;padding:0 4px;font-size:8.5px;color:#8a6a1a}
.listing .bar b{font-size:10px;color:#5a3e1d;margin-right:6px}
.listing .bar i{font-style:normal;margin-left:auto;color:var(--price);font-weight:700;font-size:10px}
.listing .spec{position:absolute;left:168px;top:33px;font-size:8.5px;color:#222;word-spacing:1px}
.listing .type{position:absolute;left:168px;top:47px;font-size:8.5px;color:#8a6a1a}
.listing .acts{position:absolute;left:165px;top:64px;width:353px;height:21px;border-top:1px solid #ddd2b8;border-bottom:1px solid #ddd2b8;display:flex;align-items:center;padding-left:4px;font-size:8.5px;color:var(--link);gap:6px}
.acts .sep{color:#999}
.acts .a{color:#555}
.news-item{left:638px;width:200px;height:44px}
.news-item .nt{position:absolute;left:0;top:0;width:38px;height:30px;background:#fff;padding:1px}
.news-item .nt div{width:100%;height:100%;background:linear-gradient(#8fa9c4,#7a5b3e 55%,#4d6e2c)}
.news-item h5{position:absolute;left:46px;top:0;width:150px;font-weight:400;font-size:9px;line-height:11.5px;color:#111}
.news-item small{position:absolute;left:46px;font-size:7px;color:#6a5f50}
.subscribe{left:639px;top:857px;width:190px;height:74px;background:linear-gradient(#ddd1b4,#cbbd9c);border:1px solid #b4a383;border-radius:4px}
.footer{left:57px;top:960px;width:786px;height:182px;background:linear-gradient(#e6d9b8,var(--page))}
.fcol h3{position:absolute;font-family:"Gelasio",serif;font-size:12.5px;font-weight:400;color:#4a3b2c}
.about{left:78px;top:999px;width:232px;font-size:9.3px;line-height:14.5px;color:#222}
.help{left:333px;top:998px;width:234px}
.help div{height:18px;border-bottom:1px solid #d9cca9;font-size:9.5px;font-weight:700;color:var(--olive);padding-left:14px;position:relative;line-height:17px}
.help div::before{content:"";position:absolute;left:2px;top:6px;border:3px solid transparent;border-left:4px solid #9a8a6a}
.quote{left:628px;top:1004px;width:190px;font-family:"Gelasio",serif;font-size:12.5px;line-height:16px;color:#3a3027}
.skyline{left:57px;top:1110px;width:786px;height:32px;background:linear-gradient(rgba(206,192,160,0),#d3c4a0)}
.bottom{left:57px;top:1142px;width:786px;height:52px;background:linear-gradient(#d7c9a6,var(--page));font-family:"Gelasio",serif;font-size:9px;color:#3a3027}
</style>
</head>
<body>
<div class="abs site-name">Dwellora</div>
<div class="abs tagline">Search from all kind of Properties</div>
<div class="abs toplinks">Welcome, Guest<span>|</span><a href="#">Sign In</a><span>|</span><a href="#">Sign Up</a></div>
<div class="abs submit-btn">Submit a Property <svg width="12" height="10" viewBox="0 0 12 10"><path d="M1 1l4 4-4 4M6 1l4 4-4 4" stroke="#fff" stroke-width="2" fill="none"/></svg></div>

<nav class="abs nav"><a>Home</a><a>Buying</a><a>Building</a><a>Selling</a><a>Our Agents</a><a>Financing</a><a>Moving</a><a>Contact</a></nav>

<section class="abs featured"></section>
<div class="abs hero"><div class="hero-img" role="img" aria-label="Photo of a brick two-storey house with a green lawn"></div></div>
<div class="abs hero-cap"><span>6051 Alder Ave</span><b>$ 12,21,323</b></div>
<div class="abs ribbon">Featured Properties</div>
<div class="abs thumb" style="top:112px"><div role="img" aria-label="Bedroom interior photo"></div></div>
<div class="abs thumb" style="top:166px"><div role="img" aria-label="Living room interior photo"></div></div>
<div class="abs thumb" style="top:219px"><div role="img" aria-label="Lounge interior photo"></div></div>
<div class="abs thumb" style="top:272px"><div role="img" aria-label="Fireplace interior photo"></div></div>

<aside class="abs agents"></aside>
<div class="abs section-title" style="left:624px;top:109px"><svg width="10" height="11" viewBox="0 0 10 11" style="vertical-align:-1px"><circle cx="5" cy="3" r="2.6" fill="#c28a4a"/><path d="M0 11c0-4 2-5.5 5-5.5S10 7 10 11z" fill="#4a6da0"/></svg> Featured Agent</div>
<div class="abs" style="left:622px;top:130px;width:213px;height:1px;background:#cdbf9f"></div>
<div class="abs agent" style="top:136px;border:0"><h4>Nolan Pryce</h4><p>Listed: 10 Properties</p><div class="photo"><div role="img" aria-label="Agent portrait"></div></div></div>
<div class="abs agent" style="top:183px"><h4>Bob Wendel</h4><p>Listed: 10 Properties</p><div class="photo"><div role="img" aria-label="Agent portrait"></div></div></div>
<div class="abs agent" style="top:230px"><h4>Ray</h4><p>Listed: 10 Properties</p><div class="photo"><div role="img" aria-label="Agent portrait"></div></div></div>
<div class="abs agent" style="top:278px"><h4>Nolan Pryce</h4><p>Listed: 10 Properties</p><div class="photo"><div role="img" aria-label="Agent portrait"></div></div></div>

<form class="abs search">
  <div class="lbl" style="left:16px;top:11px">Search Properties for : <span class="radio"></span>Buy <span class="radio" style="margin-left:18px"></span>Rent</div>
  <div class="lbl" style="left:16px;top:34px">by Location :</div>
  <div class="field select" style="left:101px;top:32px;width:209px"></div>
  <div class="lbl" style="left:22px;top:62px">Price Rage :</div>
  <div class="field select" style="left:101px;top:59px;width:209px"></div>
  <div class="lbl" style="left:24px;top:91px">Bedrooms :</div>
  <div class="field select" style="left:101px;top:88px;width:52px"></div>
  <div class="lbl" style="left:172px;top:91px">Bathrooms :</div>
  <div class="field select" style="left:253px;top:88px;width:52px"></div>
  <div class="lbl" style="left:340px;top:34px">Area (Sq. ft.) :</div>
  <div class="field" style="left:429px;top:32px;width:143px"></div>
  <div class="lbl" style="left:364px;top:61px">Keyword :</div>
  <div class="field" style="left:429px;top:59px;width:143px"></div>
  <div class="s-btn" style="left:427px;top:87px;width:144px"><svg width="12" height="12" viewBox="0 0 12 12"><circle cx="5" cy="5" r="3.5" stroke="#fff" stroke-width="1.6" fill="none"/><path d="M7.5 7.5L11 11" stroke="#fff" stroke-width="2"/></svg>Search &nbsp;Properties</div>
  <div class="divider-v"></div>
  <div class="lbl" style="left:611px;top:42px">Property ID :</div>
  <div class="field" style="left:609px;top:58px;width:143px"></div>
  <div class="s-btn" style="left:608px;top:87px;width:86px"><svg width="12" height="12" viewBox="0 0 12 12"><circle cx="5" cy="5" r="3.5" stroke="#fff" stroke-width="1.6" fill="none"/><path d="M7.5 7.5L11 11" stroke="#fff" stroke-width="2"/></svg>Search</div>
</form>

<section class="abs services">
  <div class="svc" style="left:0;width:258px;border-right:1px solid #d3c7aa">
    <svg class="abs" style="left:19px;top:10px" width="28" height="22" viewBox="0 0 28 22"><rect x="1" y="4" width="24" height="14" rx="2" fill="#9cb85a" stroke="#6b8a2e"/><circle cx="13" cy="11" r="4" fill="#e6c54a"/></svg>
    <h3>LOAN</h3><p>Lorem ipsum dolor sit amet, consectetuer adipiscing elit. Praesent aliquam, justo convallis luctus rutrum, erat nulla ferm.</p>
    <div class="more">Read More <svg width="5" height="6"><path d="M0 0l5 3-5 3z" fill="#fff"/></svg></div>
  </div>
  <div class="svc" style="left:259px;width:268px;border-right:1px solid #d3c7aa">
    <svg class="abs" style="left:22px;top:9px" width="22" height="24" viewBox="0 0 22 24"><rect x="3" y="2" width="16" height="20" fill="#b8c3cc" stroke="#6f7b85"/><path d="M6 6h3M13 6h3M6 10h3M13 10h3M6 14h3M13 14h3" stroke="#4d6a8a" stroke-width="2"/></svg>
    <h3>RENTAL</h3><p>Lorem ipsum dolor sit amet, consectetuer adipiscing elit. Praesent aliquam, justo convallis luctus rutrum, erat nulla ferm.</p>
    <div class="more" style="left:22px">Read More <svg width="5" height="6"><path d="M0 0l5 3-5 3z" fill="#fff"/></svg></div>
  </div>
  <div class="svc" style="left:528px;width:256px">
    <svg class="abs" style="left:11px;top:12px" width="22" height="22" viewBox="0 0 22 22"><path d="M11 1l4 4h-2.5v4.5H17V7l4 4-4 4v-2.5h-4.5V17H15l-4 4-4-4h2.5v-4.5H5V15l-4-4 4-4v2.5h4.5V5H7z" fill="#7fb03a"/></svg>
    <h3 style="left:38px">MOVING? LET US HELP</h3>
    <div class="abs" style="left:12px;top:36px;font-family:Gelasio,serif;font-size:16px;color:#4a4038">Call now 1-800 555 0142</div>
    <div class="abs" style="left:40px;top:57px;font-size:9px;font-weight:700;color:#333">MON - FRI 10:00 AM TO 7:00 PM</div>
    <div class="more">Read More <svg width="5" height="6"><path d="M0 0l5 3-5 3z" fill="#fff"/></svg></div>
  </div>
</section>

<main class="abs content"></main>
<div class="abs" style="left:620px;top:579px;width:1px;height:376px;background:#e0d6bd"></div>
<div class="abs section-title" style="left:72px;top:593px"><svg width="10" height="11" viewBox="0 0 10 11" style="vertical-align:-1px"><path d="M1 10V4l4-3 4 3v6z" fill="#a89a80"/></svg> Latest Property</div>
<div class="abs" style="left:481px;top:598px;font-size:8.5px;color:var(--link)">View More Properties »</div>
<div class="abs" style="left:72px;top:613px;width:518px;height:1px;background:#ddd2b8"></div>

<article class="abs listing" style="top:627px">
  <div class="pic"><div role="img" aria-label="No photo placeholder with a house outline" style="background:#ddd3bd"></div></div>
  <div class="abs" style="left:-3px;top:-3px;width:18px;height:14px;border-radius:50%;background:#f08a1c"></div>
  <div class="bar"><b>86348 Hwy 612</b>Brookvale, CA90001<i>$218,000</i></div>
  <div class="spec">7 Bed &nbsp;| &nbsp;11 Bath &nbsp;| &nbsp;14,294 Sq Ft &nbsp;| &nbsp;MLS #09-377967</div>
  <div class="type">Single Family Home</div>
  <div class="acts">✉ Email to Agent <span class="sep">|</span> <span class="a">✉ Send to Friend</span> <span class="sep">|</span> <span style="color:#e0a100">★</span> Add to Favorite</div>
</article>
<article class="abs listing" style="top:736px">
  <div class="pic"><div role="img" aria-label="Photo of a single-storey home with garden" style="background:linear-gradient(#6e8c4a,#8a6a4a 50%,#6f9a3a)"></div></div>
  <div class="bar"><b>2239 S Linden</b>Marlow, CA90001<i>$885,000</i></div>
  <div class="spec">4 Bed &nbsp;| &nbsp;5 Bath &nbsp;| &nbsp;10,994 Sq Ft &nbsp;| &nbsp;MLS #09-377958</div>
  <div class="type">Single Family Home</div>
  <div class="acts">✉ Email to Agent <span class="sep">|</span> <span class="a">✉ Send to Friend</span> <span class="sep">|</span> <span style="color:#e0a100">★</span> Add to Favorite</div>
</article>
<article class="abs listing" style="top:843px">
  <div class="pic"><div role="img" aria-label="Photo of a timber house under blue sky" style="background:linear-gradient(#4f8fd0,#9bbbd8 40%,#7a5335 60%,#5b8a3a)"></div></div>
  <div class="bar"><b>542 W Harlan</b>Pinecrest, CA90001<i>$695,000</i></div>
  <div class="spec">3 Bed &nbsp;| &nbsp;11 Bath &nbsp;| &nbsp;14,294 Sq Ft &nbsp;| &nbsp;MLS #09-377967</div>
  <div class="type">Single Family Home</div>
  <div class="acts">✉ Email to Agent <span class="sep">|</span> <span class="a">✉ Send to Friend</span> <span class="sep">|</span> <span style="color:#e0a100">★</span> Add to Favorite</div>
</article>

<div class="abs section-title" style="left:639px;top:592px"><svg width="12" height="10" viewBox="0 0 12 10" style="vertical-align:-1px"><rect x="0.5" y="0.5" width="11" height="9" fill="#eee" stroke="#888"/><path d="M2 3h8M2 5h8M2 7h5" stroke="#888"/></svg> Latest News</div>
<div class="abs" style="left:638px;top:612px;width:196px;height:1px;background:#d3c7aa"></div>
<div class="abs news-item" style="top:622px"><div class="nt"><div role="img" aria-label="News photo of a house"></div></div><h5>Integer turpis arcu, pellentesque eget</h5><small style="top:26px">12 Jun 2009 // 5 comments</small></div>
<div class="abs news-item" style="top:669px"><div class="nt"><div role="img" aria-label="News photo of an interior" style="background:linear-gradient(135deg,#6a3a1a,#d49a64)"></div></div><h5>Donec et ipsum et sapien vehicula nonummy potenti.</h5><small style="top:27px">12 Jun 2009 // 5 comments</small></div>
<div class="abs news-item" style="top:715px"><div class="nt"><div role="img" aria-label="News photo of a house"></div></div><h5>luctus rutrum, erat nulla fermentum diam, at nonummy</h5><small style="top:26px">12 Jun 2009 // 5 comments</small></div>
<div class="abs news-item" style="top:763px"><div class="nt"><div role="img" aria-label="News photo of an interior" style="background:linear-gradient(135deg,#6a3a1a,#d49a64)"></div></div><h5>Cras ultrices, nisi quis pretium sollicitudin, odio nulla</h5><small style="top:26px">12 Jun 2009 // 5 comments</small></div>
<div class="abs news-item" style="top:810px"><div class="nt"><div role="img" aria-label="News photo of a house"></div></div><h5>Cras ultrices, nisi quis pretium sollicitudin, odio nulla</h5><small style="top:26px">12 Jun 2009 // 5 comments</small></div>

<div class="abs subscribe">
  <div class="abs" style="left:9px;top:5px;font-family:Gelasio,serif;font-size:12px;font-weight:600;color:var(--link)">✉ Subscribe Now</div>
  <div class="abs" style="left:10px;top:22px;width:172px;font-size:7px;line-height:9px;color:#333">Stay updated with all our latest news enter your e-mail address here.</div>
  <div class="abs" style="left:9px;top:42px;width:129px;height:18px;background:#fff;border:1px solid #b4a383"></div>
  <div class="abs" style="left:138px;top:42px;width:42px;height:18px;background:#9c8a74;color:#fff;font-size:8px;text-align:center;line-height:18px">Submit</div>
</div>

<footer class="abs footer"></footer>
<div class="abs" style="left:316px;top:965px;width:1px;height:170px;background:#f6f0df"></div>
<div class="abs" style="left:584px;top:965px;width:1px;height:170px;background:#f6f0df"></div>
<div class="fcol"><h3 style="left:77px;top:971px">About Us</h3><h3 style="left:333px;top:971px">Mortage Help Center?</h3><h3 style="left:599px;top:971px">Testimonials</h3></div>
<p class="abs about">Aenean sagittis. Etiam leo pede, rhoncus venenatis, tristique in, vulputate at, odio. Donec et ipsum et sapien vehicula nonummy. Suspendisse potenti. Fusce varius urna id quam. Sed neque mi, varius eget, tincidunt nec, suscipit id, libero. In eget purus. Vestibulum ut nisl. &nbsp;<a href="#" style="color:var(--link)">read more »</a></p>
<div class="abs help"><div>Corvane Developers Ltd.</div><div>TKL Enterprises Housing</div><div>MRV Infrastructure</div><div>Hollis Gate Homes</div><div>Brightlane Propmart</div></div>
<div class="abs" style="left:604px;top:998px;font-family:Gelasio,serif;font-size:26px;color:#b3a68a">“</div>
<p class="abs quote">Quisque ornare risus quis ligula. Phasellus tristique purus a augue condimentum adipiscing. Aenean sagittis.</p>
<div class="abs" style="left:811px;top:1052px;font-family:Gelasio,serif;font-size:26px;color:#b3a68a">”</div>
<div class="abs skyline" role="img" aria-label="Faint city skyline silhouette"></div>
<div class="abs bottom">
  <div class="abs" style="left:16px;top:15px">© 2012 Dwellora All right reserved.</div>
  <div class="abs" style="right:15px;top:17px">Terms &amp; Conditions &nbsp;| &nbsp;FAQ &nbsp;| &nbsp;Privacy Policy</div>
</div>
</body>
</html>
```